Tidal Oak Business Cards

We need something new, fun and exciting for business cards. Our current ones are just plain and we need a design that pops. We want name, position held, phone, email on the front, and a 20% discount on the back. I have also uploaded our old business cards creative to see what we are not wanting, and how boring they were and we want something jazzed up from this, cool design and catches people attention.

```html
<!DOCTYPE html>
<html lang="en">
<head>
<meta charset="utf-8">
<title>Tidal Oak Business Cards</title>
<link href="https://fonts.googleapis.com/css2?family=Roboto:wght@400;500;700&display=swap" rel="stylesheet">
<style>
  :root {
    --backdrop: #bcbcbc;
    --card: #f1f1f0;
    --navy: #1f2b4d;
    --coral: #d9605c;
    --ink: #2a2f3d;
    --white: #ffffff;
    --faint: #dfe0e4;
  }
  * { margin: 0; padding: 0; box-sizing: border-box; }
  html, body { width: 1200px; height: 576px; overflow: hidden; }
  body {
    background: var(--backdrop);
    font-family: "Roboto", Arial, sans-serif;
    position: relative;
  }
  .card {
    position: absolute;
    background: var(--card);
    border-radius: 10px;
    overflow: hidden;
    box-shadow: 0 2px 6px rgba(0,0,0,0.18);
  }
  .card--back { left: 82px; top: 139px; width: 484px; height: 293px; }
  .card--front { left: 602px; top: 138px; width: 482px; height: 291px; }

  .brand-dot { width: 22px; height: 22px; border-radius: 50%; background: var(--coral); flex: none; }
  .brand-name { font-weight: 500; color: var(--navy); line-height: 1; white-space: nowrap; }

  /* back side */
  .brand-block {
    position: absolute; left: 0; right: 0; top: 118px;
    display: flex; align-items: center; justify-content: center; gap: 12px;
  }
  .card--back .brand-name { font-size: 46px; }
  .discount {
    position: absolute; left: 0; right: 0; top: 190px;
    display: flex; align-items: center; justify-content: center; gap: 10px;
    font-size: 13px; color: var(--ink);
  }
  .discount-badge {
    background: var(--coral); color: var(--white);
    font-weight: 700; font-size: 14px;
    padding: 5px 12px; border-radius: 14px; letter-spacing: 0.3px;
  }
  .back-site {
    position: absolute; left: 0; right: 0; top: 258px;
    display: flex; align-items: center; justify-content: center; gap: 26px;
    font-size: 12.5px; color: var(--ink);
  }
  .back-site .dash { width: 32px; height: 2px; background: var(--coral); border-radius: 1px; }
  .back-band { position: absolute; left: 0; right: 0; bottom: 0; height: 10px; display: flex; }
  .back-band span { flex: 1; }
  .back-band .navy { background: var(--navy); }
  .back-band .coral { background: var(--coral); }

  /* front side */
  .front-accent {
    position: absolute; left: 262px; top: 12px; width: 250px; height: 250px;
    border-radius: 50%; background: var(--faint);
  }
  .front-brand {
    position: absolute; left: 30px; top: 66px;
    display: flex; align-items: center; gap: 12px;
  }
  .card--front .brand-name { font-size: 44px; }
  .person { position: absolute; left: 30px; top: 166px; }
  .person-name { font-size: 19px; font-weight: 700; color: var(--navy); }
  .person-role { font-size: 12.5px; color: var(--coral); margin-top: 3px; }
  .contact {
    position: absolute; left: 274px; top: 170px;
    font-size: 12.5px; color: var(--ink); line-height: 1.45;
  }
  .contact-row { display: flex; align-items: center; gap: 10px; }
  .contact-row svg { width: 12px; height: 12px; flex: none; }
  .contact-address { margin-top: 6px; line-height: 1.5; }
  .front-band {
    position: absolute; left: 0; bottom: 0; width: 230px; height: 13px;
    background: var(--coral);
  }
  .front-tab {
    position: absolute; right: 0; bottom: 0; width: 264px; height: 36px;
    background: var(--navy);
    clip-path: polygon(16px 0, 100% 0, 100% 100%, 0 100%);
    color: var(--white); font-size: 12.5px;
    display: flex; align-items: center; justify-content: center; padding-left: 20px;
  }
</style>
</head>
<body>
  <section class="card card--back" aria-label="Card back">
    <div class="brand-block">
      <span class="brand-dot"></span>
      <span class="brand-name">Tidal Oak</span>
    </div>
    <div class="discount">
      <span class="discount-badge">20% OFF</span>
      <span>Show this card on your next visit</span>
    </div>
    <div class="back-site">
      <span class="dash"></span>
      <span>www.tidaloakco.com</span>
      <span class="dash"></span>
    </div>
    <div class="back-band"><span class="navy"></span><span class="coral"></span></div>
  </section>

  <section class="card card--front" aria-label="Card front">
    <div class="front-accent" aria-hidden="true"></div>
    <div class="front-brand">
      <span class="brand-dot"></span>
      <span class="brand-name">Tidal Oak</span>
    </div>
    <div class="person">
      <div class="person-name">Owen Hale Carter</div>
      <div class="person-role">Managing Director</div>
    </div>
    <div class="contact">
      <div class="contact-row">
        <svg viewBox="0 0 12 12" aria-hidden="true"><path fill="#d9605c" d="M1 4c0-1.5 2-3 5-3s5 1.5 5 3l-2 1-1-1.5H4L3 5 1 4zm2 2h6l1 5H2l1-5zm3 1.2a1.3 1.3 0 1 0 0 2.6 1.3 1.3 0 0 0 0-2.6z"/></svg>
        <span>555-204-7731</span>
      </div>
      <div class="contact-row">
        <svg viewBox="0 0 12 12" aria-hidden="true"><path fill="#d9605c" d="M1 2.5h10v7H1zm1 1 4 3 4-3z"/></svg>
        <span>owen@tidaloakco.com</span>
      </div>
      <div class="contact-address">87 Harbor Lane, Bay City,<br>Fern Hollow, US 204815</div>
    </div>
    <div class="front-band"></div>
    <div class="front-tab">www.tidaloakco.com</div>
  </section>
</body>
</html>
```